Home based bath & shave business wants to redesign labels

I would like to have new labels designed to fit the body lotion and bath oil bottles. We want them similar but different. The key ingredient for all of Ferrante's Bath & Shave products is olive oil.

You are free to change colors. I have attached our logo and current labels. The current labels just don't look right to me (pictures attached). I like the script font, but am willing to entertain another. I have our logo in several formats and the font, should you want it.

Target Market(s)

Women

Industry/Entity Type

Business

Font styles to use
Decorative
Script

Requirements
Must have
• Both product labels must include our logo.The logo must stay the same though to make it work with the label, you can change the color if needed.
• It should be a vertical label.
• The bottle used is a 8 oz Clear PET Tapered Naples Oval Bottle (I have attached pictures) and its dimensions are:
• Length 2.548 in / 6.472 cm
• Width 1.479 in / 3.757 cm
• Height 6.639 in / 16.863 cm

```html
<!DOCTYPE html>
<html lang="en">
<head>
<meta charset="utf-8">
<title>Ferrante's Bath &amp; Shave – Bath Oil and Body Lotion Labels</title>
<link href="https://fonts.googleapis.com/css2?family=Arimo:wght@400;700&family=Parisienne&display=swap" rel="stylesheet">
<style>
  :root {
    --page-bg: #ffffff;
    --oil-ground: #333131;
    --oil-gold: #c9a469;
    --lotion-ground: #ebc9d6;
    --lotion-plum: #5e2a6e;
  }
  html, body {
    margin: 0;
    padding: 0;
    overflow: hidden;
  }
  body {
    width: 812px;
    height: 1200px;
    background: var(--page-bg);
    position: relative;
    font-family: "Arimo", Arial, sans-serif;
  }
  .label {
    position: absolute;
    width: 278px;
    height: 448px;
  }
  .label--oil { left: 54px; top: 441px; color: var(--oil-gold); }
  .label--lotion { left: 468px; top: 444px; color: var(--lotion-plum); }
  .label__shape {
    position: absolute;
    inset: 0;
  }
  .brand-name {
    position: absolute;
    left: 0;
    right: 0;
    text-align: center;
    font-family: "Arimo", Arial, sans-serif;
    font-weight: 700;
    line-height: 1;
  }
  .brand-name__main {
    display: block;
    font-size: 20px;
    letter-spacing: 0.5px;
  }
  .brand-name__sub {
    display: block;
    font-size: 7px;
    letter-spacing: 1px;
    margin-top: 4px;
    text-transform: uppercase;
  }
  .label--oil .brand-name { top: 98px; }
  .label--lotion .brand-name { top: 101px; }
  .product-title {
    position: absolute;
    left: 0;
    right: 0;
    text-align: center;
    font-family: "Parisienne", cursive;
    font-weight: 400;
    font-size: 40px;
    line-height: 1;
    margin: 0;
  }
  .label--oil .product-title { top: 214px; }
  .label--lotion .product-title { top: 206px; font-size: 38px; }
  .ingredients {
    position: absolute;
    left: 20px;
    right: 20px;
    text-align: center;
    margin: 0;
  }
  .label--oil .ingredients {
    top: 345px;
    font-size: 13.5px;
    line-height: 17px;
  }
  .label--lotion .ingredients {
    top: 290px;
    font-size: 12.3px;
    line-height: 14.6px;
  }
</style>
</head>
<body>

  <section class="label label--oil" aria-label="Bath Oil label">
    <svg class="label__shape" width="278" height="448" viewBox="0 0 278 448" aria-hidden="true">
      <ellipse cx="139" cy="224" rx="139" ry="224" fill="var(--oil-ground)"/>
      <ellipse cx="139" cy="224" rx="127" ry="211" fill="none" stroke="var(--oil-gold)" stroke-width="2"/>
    </svg>
    <div class="brand-name">
      <span class="brand-name__main">FERRANTE'S</span>
      <span class="brand-name__sub">Bath &amp; Shave</span>
    </div>
    <h2 class="product-title">Bath Oil</h2>
    <p class="ingredients">Ingredients:<br>Olive oil, grepeseed oil<br>and fragrance oil.</p>
  </section>

  <section class="label label--lotion" aria-label="Body Lotion label">
    <svg class="label__shape" width="278" height="448" viewBox="0 0 278 448" aria-hidden="true">
      <ellipse cx="139" cy="224" rx="139" ry="224" fill="var(--lotion-ground)"/>
      <ellipse cx="139" cy="224" rx="129" ry="213" fill="none" stroke="var(--lotion-plum)" stroke-width="2.5"/>
    </svg>
    <div class="brand-name">
      <span class="brand-name__main">FERRANTE'S</span>
      <span class="brand-name__sub">Bath &amp; Shave</span>
    </div>
    <h2 class="product-title">Body Lotion</h2>
    <p class="ingredients">Ingredients:<br>Water, Olive Oil<br>Aloe Vera Juice, Avocado Oil<br>Rice Bran Oil, Emulsiwax-50<br>Glycerin, Stearyl Alcohol<br>Oat Extract, DL Panthenol<br>Preservaphen, Vitamin E<br>Buckthom Extract<br>and fragrance oil.</p>
  </section>

</body>
</html>
```